Natural Supplement Co Needs Label Makeover

Our company's success began with our main product, an amino acid blend that aids in fat metabolism, called Vantorel. Since then we continue to expand the product line that now includes a detox called Vantopure, and probiotic called Vantoflora, as well as 3 others, for a total of 6 products/ labels.
Our original design/logo had more of an 'old-timey' feel (see attached 2-product photo). We are looking for a fresh label design update for the product line which reflects the range of supplements as cohesive and individual parts of an overall health plan/strategy (see attached 'Logo Update Test' as just one idea we had in-house, you need not consider it as a starting point).

Target Market(s)

women 25-45

Industry/Entity Type

Health And Wellness

Requirements
Must have
• consistent theme with confident look
Nice to have
• Each product (ie. "Vantorel") has a few-word descriptor: ("Fat-Burning Amino Acids") that should be planned on including as part of each label.
Should not have
• NO 'streamlined' or graphic interpretations of the human body, or figurative image

```html
<!DOCTYPE html>
<html lang="en">
<head>
<meta charset="utf-8">
<title>Vantorel Garcinia Label</title>
<link href="https://fonts.googleapis.com/css2?family=Oswald:wght@600;700&family=Open+Sans:wght@400;600&family=Roboto:wght@700&display=swap" rel="stylesheet">
<style>
  :root {
    --backdrop: #e9e9ea;
    --label-white: #ffffff;
    --brand-purple: #7a3d86;
    --brand-purple-light: #8e4f9a;
    --ink-dark: #2b2b2b;
    --ink-grey: #6e6e6e;
  }
  * { margin: 0; padding: 0; box-sizing: border-box; }
  html, body { width: 1200px; height: 1137px; overflow: hidden; }
  body { background: var(--backdrop); position: relative; font-family: "Open Sans", Arial, sans-serif; }

  .label {
    position: absolute; left: 200px; top: 90px;
    width: 800px; height: 960px;
    background: var(--label-white);
    box-shadow: 0 6px 24px rgba(0,0,0,0.08);
    overflow: hidden;
  }
  .label__band { position: absolute; left: 0; top: 0; width: 800px; height: 340px; display: block; }

  .brand {
    position: absolute; left: 120px; top: 128px;
    display: flex; align-items: center; gap: 30px;
  }
  .brand__name {
    font-family: "Open Sans", Arial, sans-serif; font-weight: 600;
    font-size: 86px; color: var(--label-white); letter-spacing: -1px; line-height: 1;
  }
  .brand__dot { width: 36px; height: 36px; border-radius: 50%; background: var(--label-white); }

  .product-name { position: absolute; left: 0; top: 0; width: 800px; height: 0; }
  .product-name__lead {
    position: absolute; left: 56px; top: 442px;
    font-family: "Oswald", "Arial Narrow", sans-serif; font-weight: 700;
    font-size: 186px; line-height: 0.9; color: var(--ink-dark); letter-spacing: -5px;
  }
  .product-name__tail {
    position: absolute; left: 346px; top: 452px;
    font-family: "Oswald", "Arial Narrow", sans-serif; font-weight: 700;
    font-size: 108px; line-height: 0.9; color: var(--ink-dark); letter-spacing: 18px;
  }
  .product-name__bar {
    position: absolute; left: 372px; top: 574px;
    width: 346px; height: 26px; background: var(--brand-purple);
  }

  .descriptor {
    position: absolute; left: 150px; top: 632px;
    font-family: "Roboto", Arial, sans-serif; font-weight: 700;
    font-size: 35px; color: var(--ink-grey); letter-spacing: 2px; line-height: 1;
    white-space: nowrap;
  }

  .claim {
    position: absolute; left: 118px; top: 716px;
    width: 562px; height: 62px;
    border: 3px solid var(--brand-purple);
    display: flex; align-items: center; justify-content: center;
    font-size: 34px; color: var(--brand-purple); letter-spacing: 1.5px;
  }
  .claim-bracket {
    position: absolute; left: 190px; top: 778px; width: 420px; height: 52px;
    border: 2px solid var(--ink-grey); border-top: none;
  }
  .claim-sub {
    position: absolute; left: 190px; top: 798px; width: 420px;
    text-align: center; font-size: 32px; color: var(--ink-dark); line-height: 1;
  }
  .claim-sub span { background: var(--label-white); padding: 0 14px; position: relative; top: 16px; }

  .count {
    position: absolute; right: 44px; top: 878px;
    font-family: "Open Sans", Arial, sans-serif; font-weight: 600;
    font-size: 33px; color: var(--brand-purple); letter-spacing: 0.5px;
  }
</style>
</head>
<body>
  <main class="label">
    <svg class="label__band" viewBox="0 0 800 340" aria-hidden="true">
      <path d="M0 0 H800 V250 C560 275 300 318 0 332 Z" fill="var(--brand-purple)"/>
      <path d="M380 0 H520 V266 C470 273 420 279 380 284 Z" fill="var(--brand-purple-light)" opacity="0.45"/>
    </svg>

    <div class="brand">
      <span class="brand__name">Vantorel</span>
      <span class="brand__dot"></span>
    </div>

    <h1 class="product-name" aria-label="Garcinia">
      <span class="product-name__lead">GAR</span>
      <span class="product-name__tail">CINIA</span>
      <span class="product-name__bar"></span>
    </h1>

    <p class="descriptor">SUPPORTS APPETITE CONTROL</p>

    <p class="claim">All Natural Supplement</p>
    <div class="claim-bracket"></div>
    <p class="claim-sub"><span>Dietary Supplement</span></p>

    <p class="count">60 CAPSULES</p>
  </main>
</body>
</html>
```